Booklet Cover Design Project

Booklet cover designs - I have uploaded a couple of examples of previous covers - they should match these in concept!.

4 covers using the same theme :

1
Work Health and Safety (Medical)
KTRNPL647

2. Maintain Patient Records
KTRGOF528

3. Prepare and Process Medical Accounts
KTRGOF529

4. Confidentiality, Privacy and Security in a Medical Office
KTRGOF586

** I have uploaded a couple of samples from previous work - please use a similar style for consistency. Suggested photo samples attached.

• Consistency of theme

```html
<!DOCTYPE html>
<html lang="en">
<head>
<meta charset="utf-8">
<title>Maintain Patient Records – Booklet Cover</title>
<link href="https://fonts.googleapis.com/css2?family=Roboto:wght@400;500;700&display=swap" rel="stylesheet">
<style>
  :root {
    --page-bg: #e3e4e6;
    --cover-paper: #f5f5f7;
    --tab-navy: #1f3a58;
    --title-blue: #3c549f;
    --band-navy: rgba(44, 62, 128, 0.92);
    --tint-violet: rgba(120, 120, 190, 0.55);
    --rule-gold: #b39a5e;
    --logo-ink: #2c3e5c;
    --white: #ffffff;
  }
  * { margin: 0; padding: 0; box-sizing: border-box; }
  html, body {
    width: 1200px;
    height: 894px;
    overflow: hidden;
    background: var(--page-bg);
    font-family: "Roboto", Arial, sans-serif;
  }
  .booklet {
    position: absolute;
    left: 360px;
    top: 106px;
    width: 480px;
    height: 682px;
    background: var(--cover-paper);
    overflow: hidden;
  }
  .unit-tab {
    position: absolute;
    left: 0;
    top: 0;
    width: 131px;
    height: 36px;
    background: var(--tab-navy);
    border-bottom-right-radius: 6px;
    color: var(--white);
    font-weight: 700;
    font-size: 13.5px;
    letter-spacing: 0.2px;
    line-height: 36px;
    padding-left: 29px;
  }
  .institute {
    position: absolute;
    left: 0;
    right: 0;
    top: 64px;
    display: flex;
    flex-direction: column;
    align-items: center;
    gap: 8px;
  }
  .institute-mark {
    width: 34px;
    height: 34px;
    background: var(--logo-ink);
  }
  .institute-name {
    color: var(--logo-ink);
    font-weight: 500;
    font-size: 8.5px;
    letter-spacing: 0.8px;
    text-align: center;
    line-height: 1.25;
  }
  .cover-title {
    position: absolute;
    left: 0;
    right: 0;
    top: 182px;
    text-align: center;
    color: var(--title-blue);
    font-weight: 500;
    font-size: 30px;
    letter-spacing: -0.2px;
  }
  .cover-photo {
    position: absolute;
    left: 0;
    top: 267px;
    width: 480px;
    height: 415px;
    background: linear-gradient(90deg, #b98a8e 0%, #d9c2b8 35%, #eef0f3 55%, #8b8fa8 72%, #c78f98 100%);
  }
  .photo-tint {
    position: absolute;
    left: 344px;
    top: 267px;
    width: 136px;
    height: 415px;
    background: linear-gradient(180deg, rgba(120,120,190,0.25) 0%, var(--tint-violet) 85%);
  }
  .author-band {
    position: absolute;
    left: 0;
    top: 572px;
    width: 480px;
    height: 44px;
    background: var(--band-navy);
    display: flex;
    align-items: center;
    justify-content: center;
    gap: 8px;
    color: var(--white);
    font-size: 11.5px;
  }
  .author-band .rule {
    width: 28px;
    height: 1px;
    background: var(--rule-gold);
  }
</style>
</head>
<body>
  <main class="booklet">
    <div class="unit-tab">KTRGOF528</div>

    <div class="institute">
      <div class="institute-name">HARBOURLINE INSTITUTE<br>OF TRAINING</div>
      <div class="institute-mark"></div>
    </div>

    <h1 class="cover-title">Maintain Patient Records</h1>

    <div class="cover-photo" role="img" aria-label="Photo of a medical records room with shelves of colour-coded patient files and a staff member reaching for a folder"></div>
    <div class="photo-tint"></div>

    <div class="author-band">
      <span class="rule"></span>
      <span class="author">Written and compiled by Mara Ellison</span>
      <span class="rule"></span>
    </div>
  </main>
</body>
</html>
```